Brackwell Engineering Inc. Marketing Brochure

need a brochure designed for Brackwell Engineering Inc. It would follow the theme of www.brackwelleng.ca. It would be ~7" x 9" in size. Full Color. 4 pages. Please refer to BrackwellENG.ca to get the description of our services. The text font will be in the attached documents also. The theme must be industrial but also smart telling the customer that we use the latest in 3d cadworx to build our facilities. https://www.lookvarne.ca/find?q=3d+cadworx+images&type=img&src=qx&ctx=1&ref=MqTrodLP48vnzaX%253A%252C_2p9HbeW_4kjsT%252C_&tok=ZkwpRmq83LuxnVD-KolQW71-h3pjk_PRat&sa=Y&vid=9bhPRmxTy4kLmWf8KbQn1jLqPwRtsYcVb4HkTzXqW2pDcGhWqY#imgid=RK8M_4x2pzqm7N:&imgref=MqTrodLP48vnzaX:

Industry/Entity Type

Oil And Gas Exploration

Requirements
Must have
• a 7" x 9" brochure that is snappy, smart and crisp along the same lines at the brackwelleng.ca website.
Nice to have
• it must include the "services" listed on the brackwelleng.ca website
• It must really highlight the brand of name Brackwell Engineering Inc. AND the polar bear.
• Mission Statement: Brackwell Engineering Inc. offers fit-for-purpose, pragmatic EPCM (Engineering, Procurement and Construction Management) and Asset Management Consulting (MOC) in a timely, cost effective manner built on the foundations of safety, environmental protection and cost control.
Should not have
• it must not be too overly "wordy". We are selling an IMAGE and a BRAND here more than anything.
• Remove/do not include the Brackwell Engineering is Back paragraph... I want to move my messaging away from that theme.

```html
<!DOCTYPE html>
<html lang="en">
<head>
<meta charset="utf-8">
<title>Brackwell Engineering Inc. – Services Brochure</title>
<link rel="stylesheet" href="https://fonts.googleapis.com/css2?family=Montserrat:wght@400;500;600;700;800&display=swap">
<style>
  :root {
    --backdrop: #c4c8d1;
    --paper: #ececec;
    --charcoal: #333333;
    --ink: #2a2a2a;
    --brand-red: #e2323f;
    --red-light: #ea4c57;
    --white: #ffffff;
    --rule: #777777;
  }
  * { box-sizing: border-box; margin: 0; padding: 0; }
  html, body {
    width: 1200px; height: 864px; overflow: hidden;
    background: var(--backdrop);
    font-family: "Montserrat", Arial, sans-serif;
  }
  .spread {
    position: absolute; left: 40px; top: 72px;
    width: 1120px; height: 720px; overflow: hidden;
    box-shadow: 0 18px 40px rgba(0,0,0,.18);
  }
  .spread-shapes { position: absolute; inset: 0; }
  .services-title {
    position: absolute; left: 36px; top: 150px;
    color: var(--charcoal); font-weight: 800; font-size: 30px;
    line-height: 1.15; letter-spacing: .5px; text-transform: uppercase;
  }
  .service-col { position: absolute; }
  .service-col h3 {
    color: var(--white); font-weight: 700; font-size: 18px; margin-bottom: 14px;
  }
  .service-col ul { list-style: none; }
  .service-col li {
    color: var(--brand-red); font-size: 14px; font-weight: 500;
    line-height: 1.2; margin-bottom: 17px;
  }
  .col-epcm { left: 318px; top: 62px; width: 200px; }
  .col-asset { left: 582px; top: 62px; width: 240px; }
  .col-auto { left: 858px; top: 50px; width: 240px; }
  .col-auto li { margin-bottom: 14px; }
  .col-asbuild { left: 866px; top: 214px; width: 240px; }
  .col-asbuild li { margin-bottom: 14px; }
  .offer { position: absolute; left: 48px; top: 470px; }
  .offer-big {
    color: var(--brand-red); font-weight: 800; font-size: 92px;
    line-height: .9; letter-spacing: 2px;
  }
  .offer-small {
    color: var(--ink); font-weight: 700; font-size: 29px;
    letter-spacing: 1px; margin-top: 10px;
  }
  .contact { position: absolute; left: 596px; top: 448px; color: var(--ink); }
  .contact h2 { font-weight: 800; font-size: 34px; line-height: 1.2; margin-bottom: 12px; }
  .contact-line {
    display: flex; align-items: center; gap: 14px;
    font-size: 22px; font-weight: 500; line-height: 1.1; margin-bottom: 13px;
  }
  .contact-line svg { width: 22px; height: 22px; flex: none; fill: var(--ink); }
</style>
</head>
<body>
<main class="spread">
  <svg class="spread-shapes" viewBox="0 0 1120 720" width="1120" height="720">
    <rect width="1120" height="720" fill="var(--paper)"/>
    <rect x="0" y="26" width="1120" height="380" fill="var(--charcoal)"/>
    <polygon points="1000,0 1120,0 1120,26 980,26" fill="var(--brand-red)" opacity=".9"/>
    <polygon points="0,0 290,190 0,440" fill="var(--brand-red)" stroke="var(--paper)" stroke-width="10" stroke-linejoin="miter"/>
    <line x1="524" y1="92" x2="524" y2="392" stroke="var(--rule)" stroke-width="1.5"/>
    <line x1="838" y1="50" x2="838" y2="362" stroke="var(--rule)" stroke-width="1.5"/>
    <polygon points="532,458 552,474 246,720 208,720" fill="var(--charcoal)"/>
    <polygon points="560,474 560,720 262,720" fill="var(--brand-red)"/>
    <polygon points="600,406 1120,406 1120,560 1010,720 560,720 560,460" fill="var(--brand-red)"/>
    <line x1="560" y1="0" x2="560" y2="720" stroke="rgba(0,0,0,.08)" stroke-width="2"/>
  </svg>

  <h1 class="services-title">Our<br>Services</h1>

  <section class="service-col col-epcm">
    <h3>EPCM</h3>
    <ul>
      <li>Oil &amp; Gas Pipelines</li>
      <li>Debottlenecking</li>
      <li>Compression</li>
      <li>Refrigeration</li>
      <li>Oil Batteries</li>
      <li>Hazops</li>
      <li>Process Reviews<br>and capacity studies</li>
    </ul>
  </section>

  <section class="service-col col-asset">
    <h3>Asset Management</h3>
    <ul>
      <li>Management of Change (MOC)</li>
      <li>EPAP Programs</li>
      <li>Maintainance<br>Management</li>
      <li>Integrity Management</li>
      <li>Regulatory Submissions</li>
      <li>Suspended Well<br>Programs</li>
    </ul>
  </section>

  <section class="service-col col-auto">
    <h3>Automation</h3>
    <ul>
      <li>PLC's</li>
      <li>RTU's</li>
      <li>Control Systems</li>
      <li>Field Programming</li>
    </ul>
  </section>

  <section class="service-col col-asbuild">
    <h3>As-Building</h3>
    <ul>
      <li>3D Site &amp; Piping</li>
      <li>Laser Scanning</li>
      <li>Complete As-Built<br>Site Drawing Package</li>
    </ul>
  </section>

  <div class="offer">
    <div class="offer-big">FREE</div>
    <div class="offer-small">CONSULTATION</div>
  </div>

  <section class="contact">
    <h2>Contact Us</h2>
    <div class="contact-line">
      <svg viewBox="0 0 24 24"><path d="M12 2a7 7 0 0 0-7 7c0 5 7 13 7 13s7-8 7-13a7 7 0 0 0-7-7zm0 9.5A2.5 2.5 0 1 1 12 6.5a2.5 2.5 0 0 1 0 5z"/></svg>
      <span>Brackwell Engineering Inc.<br>Calgary, Alberta, Canada</span>
    </div>
    <div class="contact-line">
      <svg viewBox="0 0 24 24"><path d="M6.6 10.8a15 15 0 0 0 6.6 6.6l2.2-2.2a1 1 0 0 1 1-.25 11.4 11.4 0 0 0 3.6.57 1 1 0 0 1 1 1V20a1 1 0 0 1-1 1A17 17 0 0 1 3 4a1 1 0 0 1 1-1h3.5a1 1 0 0 1 1 1c0 1.25.2 2.45.57 3.57a1 1 0 0 1-.25 1z"/></svg>
      <span>(403) 555-0147</span>
    </div>
    <div class="contact-line">
      <svg viewBox="0 0 24 24"><path d="M2 5h20v14H2zm2 2v.5l8 5 8-5V7l-8 5z"/></svg>
      <span>contactus@brackwelleng.ca</span>
    </div>
    <div class="contact-line">
      <svg viewBox="0 0 24 24"><path d="M12 2a10 10 0 1 0 0 20 10 10 0 0 0 0-20zm6.9 6h-3a15 15 0 0 0-1.4-3.9A8 8 0 0 1 18.9 8zM12 4a13 13 0 0 1 1.9 4h-3.8A13 13 0 0 1 12 4zM4.3 14a8 8 0 0 1 0-4h3.4a16 16 0 0 0 0 4zm.8 2h3a15 15 0 0 0 1.4 3.9A8 8 0 0 1 5.1 16zm3-8h-3a8 8 0 0 1 4.4-3.9A15 15 0 0 0 8.1 8zM12 20a13 13 0 0 1-1.9-4h3.8A13 13 0 0 1 12 20zm2.3-6H9.7a14 14 0 0 1 0-4h4.6a14 14 0 0 1 0 4zm.2 5.9a15 15 0 0 0 1.4-3.9h3a8 8 0 0 1-4.4 3.9zm1.8-5.9a16 16 0 0 0 0-4h3.4a8 8 0 0 1 0 4z"/></svg>
      <span>BrackwellEng.ca</span>
    </div>
  </section>
</main>
</body>
</html>
```